Business Card Design Project

Business card design with a funky, clean, modern design. Business is an immigration consultancy. Client base will be Canadian employers wanting to hire or retain foreign workers and foreign nationals wanting to immigrate to Canada.

Full color possible, but should incorporate red/white/black as per the logo to be provided. Double sided card design.

Target Market(s)

Canadian employers looking to hire/retain staff and also foreign nationals immigrating to Canada

Industry/Entity Type

Business

Requirements
Must have
• Logo (to be provided)
Name (Marla Voskuil, Immigration Consultant)
Phone (604) 731-5562
E-mail: marla@tallowbrookmigration.example
Web: www.tallowbrookmigration.example

Nice to have
• Tag Line
Clean, modern style

```html
<!DOCTYPE html>
<html lang="en">
<head>
<meta charset="utf-8">
<title>Tallowbrook Migration – Business Card</title>
<link rel="stylesheet" href="https://fonts.googleapis.com/css2?family=Open+Sans:wght@400;700&display=swap">
<style>
  :root {
    --stage-light: #f7f7f7;
    --stage-dark: #d9d9d9;
    --card-black: #000000;
    --brand-red: #e0202a;
    --deep-red: #b3121b;
    --ink-white: #ffffff;
    --ink-grey: #d6d6d6;
  }
  * { margin: 0; padding: 0; box-sizing: border-box; }
  html, body { width: 927px; height: 1200px; overflow: hidden; }
  body {
    position: relative;
    font-family: "Open Sans", Arial, sans-serif;
    background: radial-gradient(ellipse 60% 50% at 50% 48%, var(--stage-light) 0%, #ececec 55%, var(--stage-dark) 100%);
  }
  .card {
    position: absolute;
    left: 203px;
    width: 576px;
    height: 329px;
    background: var(--card-black);
    box-shadow: 0 1px 3px rgba(0,0,0,0.25);
  }
  .card--front { top: 223px; }
  .card--back { top: 636px; }

  .brand-lockup {
    position: absolute;
    display: flex;
    flex-direction: column;
    align-items: center;
  }
  .brand-lockup__dot {
    border-radius: 50%;
    background: linear-gradient(160deg, var(--brand-red), var(--deep-red));
  }
  .brand-lockup__name {
    color: var(--ink-white);
    font-weight: 700;
    text-transform: uppercase;
    text-align: center;
    line-height: 1.15;
  }
  .card--front .brand-lockup {
    left: 0; right: 0; top: 62px;
  }
  .card--front .brand-lockup__dot { width: 112px; height: 112px; margin-bottom: 22px; }
  .card--front .brand-lockup__name { font-size: 27px; letter-spacing: 1px; }
  .card--front .brand-lockup__name span { display: block; font-size: 16px; letter-spacing: 4px; }

  .front-web {
    position: absolute;
    left: 0; right: 0; top: 299px;
    text-align: center;
    font-size: 9px;
    color: var(--brand-red);
  }

  .card--back .brand-lockup {
    left: 372px; top: 26px; width: 170px;
  }
  .card--back .brand-lockup__dot { width: 78px; height: 78px; margin-bottom: 10px; }
  .card--back .brand-lockup__name { font-size: 13px; letter-spacing: 1px; }

  .holder {
    position: absolute;
    left: 32px; top: 158px;
  }
  .holder__name {
    color: var(--brand-red);
    font-weight: 700;
    font-size: 20px;
    line-height: 1.2;
  }
  .holder__title {
    color: var(--ink-grey);
    font-size: 13px;
    margin-left: 45px;
    margin-top: 1px;
  }
  .contact {
    position: absolute;
    left: 32px; top: 256px;
    list-style: none;
  }
  .contact__row { display: flex; align-items: baseline; height: 30px; }
  .contact__label {
    color: var(--deep-red);
    font-weight: 700;
    font-size: 20px;
    margin-right: 6px;
  }
  .contact__value { color: var(--ink-white); font-size: 16px; }
</style>
</head>
<body>
  <section class="card card--front" aria-label="Card front">
    <div class="brand-lockup">
      <div class="brand-lockup__dot"></div>
      <div class="brand-lockup__name">Tallowbrook<span>Migration</span></div>
    </div>
    <p class="front-web">www.tallowbrookmigration.example</p>
  </section>

  <section class="card card--back" aria-label="Card back">
    <div class="brand-lockup">
      <div class="brand-lockup__dot"></div>
      <div class="brand-lockup__name">Tallowbrook Migration</div>
    </div>
    <div class="holder">
      <p class="holder__name">Marla Voskuil</p>
      <p class="holder__title">RCIC</p>
    </div>
    <ul class="contact">
      <li class="contact__row"><span class="contact__label">Phone</span><span class="contact__value">(604) 731-5562</span></li>
      <li class="contact__row"><span class="contact__label">E-mail</span><span class="contact__value">marla@tallowbrookmigration.example</span></li>
    </ul>
  </section>
</body>
</html>
```